Domestic Building Company requires professional webpage

We have an existing webpage that was never completed. We are a growing building company specialising in domestic building, renovations and commercial maintenance. We liaise closely with each of our clients to provide quality service they would be happy to recommend. Our easy approachable staff give our clients the confidence to discuss their needs and changes they may have along the way.
Our main source of new customers have been from recommendations of existing clients.
We would like our webpage to reflect our eye for detail and showcase our previous work.
The colour theme should be the same as the colours of our logo.
We would like the main page to really stand out with a slideshow of our pictures of works we have completed.
We would like the tabs to remain the same - Home, About Us, Our Services, Contact us.
In the Our Services section we would like each sub heading to be a link where viewers can see pictures from previous work we have completed.
Our current web page is www.ferncastconstruct.com.au

```html
<!DOCTYPE html>
<html lang="en">
<head>
<meta charset="utf-8">
<title>About Us | Ferncast Construct</title>
<link rel="stylesheet" href="https://fonts.googleapis.com/css2?family=Arvo:wght@400;700&display=swap">
<style>
  :root {
    --brand-blue: #1f5fa8;
    --brand-green: #8cc63f;
    --heading-blue: #1e8fff;
    --link-blue: #2a8ef0;
    --nav-dark: #1c2730;
    --nav-mid: #34424d;
    --tab-grey: #7f97aa;
    --tab-grey-light: #a9bccb;
    --tab-active: #2b8cf2;
    --tab-active-light: #5aaefc;
    --tab-text: #e6edf3;
    --text: #2b2b2b;
    --footer-text: #555b55;
    --page-top: #f8fff8;
    --page-bottom: #b2ffac;
    --rule: #9aa59a;
    --badge-border: #2a67b8;
  }
  * { box-sizing: border-box; margin: 0; padding: 0; }
  html, body {
    width: 1153px;
    height: 1200px;
    overflow: hidden;
  }
  body {
    position: relative;
    font-family: "Arvo", Georgia, serif;
    color: var(--text);
    background: linear-gradient(to bottom, var(--page-top) 0px, #ffffff 140px, #e2ffe0 200px, #c8ffc4 700px, var(--page-bottom) 1200px);
  }
  .site-header {
    position: absolute;
    top: 0; left: 0;
    width: 1153px;
    height: 151px;
    display: flex;
    align-items: center;
    justify-content: center;
    gap: 14px;
  }
  .brand-name {
    font-family: "Arvo", Georgia, serif;
    font-weight: 700;
    font-size: 44px;
    color: var(--brand-blue);
    letter-spacing: 0.5px;
  }
  .brand-mark {
    width: 58px;
    height: 58px;
    background: var(--brand-green);
  }
  .main-nav {
    position: absolute;
    top: 151px; left: 0;
    width: 1153px;
    height: 44px;
    background: linear-gradient(to bottom, var(--nav-mid), var(--nav-dark));
  }
  .nav-tabs {
    position: absolute;
    top: 6px; left: 314px;
    display: flex;
    gap: 2px;
    list-style: none;
  }
  .nav-tab {
    height: 32px;
    display: flex;
    align-items: center;
    justify-content: center;
    font-family: "Arvo", Georgia, serif;
    font-weight: 700;
    font-size: 14px;
    color: var(--tab-text);
    text-transform: uppercase;
    background: linear-gradient(to bottom, var(--tab-grey-light), var(--tab-grey));
    border-radius: 6px 6px 0 0;
  }
  .nav-tab.is-current {
    background: linear-gradient(to bottom, var(--tab-active-light), var(--tab-active));
    color: #10305a;
  }
  .tab-home { width: 97px; }
  .tab-about { width: 129px; }
  .tab-services { width: 163px; }
  .tab-contact { width: 150px; }
  .page-content {
    position: absolute;
    top: 230px; left: 0;
    width: 1153px;
  }
  .page-title {
    font-family: "Arvo", Georgia, serif;
    font-weight: 700;
    font-size: 28px;
    color: var(--heading-blue);
    padding-left: 3px;
    line-height: 40px;
  }
  .intro-text {
    width: 1120px;
    margin-left: 19px;
    font-size: 13.5px;
    line-height: 24px;
    text-indent: 20px;
  }
  .intro-text.first { margin-top: 17px; }
  .intro-text.second { margin-top: 57px; text-indent: 13px; }
  .member-badge {
    position: absolute;
    top: 507px; left: 469px;
    width: 228px;
    height: 105px;
    background: #ffffff;
    border: 2px solid var(--badge-border);
  }
  .site-footer {
    position: absolute;
    top: 1086px; left: 14px;
    width: 1139px;
    border-top: 2px solid var(--rule);
    text-align: center;
    padding-top: 29px;
    font-size: 14px;
    color: var(--footer-text);
  }
  .site-footer .company-link { color: var(--link-blue); }
</style>
</head>
<body>
  <header class="site-header">
    <span class="brand-name">Ferncast Construct</span>
    <span class="brand-mark" aria-hidden="true"></span>
  </header>

  <nav class="main-nav" aria-label="Main">
    <ul class="nav-tabs">
      <li class="nav-tab tab-home">Home</li>
      <li class="nav-tab tab-about is-current">About Us</li>
      <li class="nav-tab tab-services">Our Services</li>
      <li class="nav-tab tab-contact">Contact Us</li>
    </ul>
  </nav>

  <main class="page-content">
    <h1 class="page-title">About Ferncast Construct</h1>
    <p class="intro-text first">Hi my name is Reuben, I am a qualified Carpenter / Builder having been in the industry for the past 12 years and have been self employed for the past 7 years. I have worked on various projects from residential housing through to large commercial projects. Throughout my experience as a Carpenter / Builder I have developed an eye for detail which is shown throughout my work. I take pride in delivering services and product that would always be recommended.</p>
    <p class="intro-text second">I have recently purchased my first property in the area after moving south from Sydney. I enjoy keeping active and when I am not at work you will find me on the golf course or out in the surf.</p>
  </main>

  <div class="member-badge" role="img" aria-label="Builders association membership badge"></div>

  <footer class="site-footer">
    Copyright 2014 <span class="company-link">Ferncast Construct Pty Ltd</span> | ABN: 48 615 207 339 | Lic: 304518B
  </footer>
</body>
</html>
```